eBook cover for new contemporary fiction

I need a front and back cover design for my newly finished ebook. It is entitled "Paper Crown". The following should help in understanding the story line:
Back Cover blurb:

Dale and Rhoda Pembury ran a successful courier company-until the Internet changed the way documents were delivered. Now, through a series of tragic events and poor financial decisions, Dale has begun to ask himself some tough questions.

To what length would Dale go to save himself from the effects of poor financial decisions? How far can he sink to hide personal failure from his wife and children? Could he burn his house down to collect insurance? Could he fake his own death to give his family what they deserve? Or could he even kill his wife and children to end their struggles?

While Dale is trapped in his own personal hell, Rhoda discovers what she thinks may be an anodyne for their financial ailments. Can it save them in time? Or will it destroy them all?

Written by an experienced (now reformed) telemarketer, the insidious greed and trickery of the industry is revealed in a story that will find you grinding your teeth and clenching your jaw. Not only is Paper Crown entertaining, but it is a welcome manifesto of true confessions by a former insider of the industry.

(end of back cover)

PLEASE NOTE: I have received a number of decent submissions but they are all missing the emotions behind what I need. I wrote this to one of the artists, perhaps it will help you:
I have really been trying to digest your cover art and what it is I'm trying to portray. I still like this design but have finally identified what it is that has kept me uneasy about it. The guy you have on the cover doesn't fit the image of the protagonist. There is a disconnect that I cannot not reconcile in my my mind. In the book, the salesman rides a Vantor and drives a convertible Delvane. He is a womanizer and an admitted alcoholic, though thrives on both. He is very good at what he does and is continually driven to achieve more. The reason I liked the caricature of the sample art I posted is that it shows sleazy class. It portrays the slickness of a master manipulator. Having said that, I am not convinced that this cover has to have "someone" to portray all the things I have just mentioned. Am I making any sense?

I really want to portray Greed, Lust, and Fear - or at least two out of the three. Displaying the bottle of Paper Crown certainly represents the greed but I don't get a sense of what the book is about. You are probably too busy, but did you read the sample chapters? There is real heartache and tragedy in a family and the salesman attempts to exploit that.

Let me know what you think of all this. Thanks for listening.

END NOTE

Also, if you are so inclined, there are 9 chapters at PaperCrownTheBook.test that will give you a great understanding of what the cover needs to portray. (The site is under development but the chapters are there to read.)

This is my first use of ArtQuorum and as such I am sure I have not given you all the information you need. Please do not hesitate to ask. I will respond as quickly as I can.

The authors name should appear as Warren T. Ashby.

40 year-olds and up, both male and female.

Financial

• The specs must satisfy Borealis Leaf requirements for ebook covers.
The title of: Paper Crown
The author's name of: Warren T. Ashby
The tagline of: A Modern Tale of Greed, Lust, and Fear
• Purely informational: the attached file is a cover I had put together from artwork I found on the Internet. I tracked the artist down to discover that the piece had been commissioned for another company and is not available. However, I love the color, the imagery, the depth of message within the art. I am going at this project with an open mind, the sample is just one that I loved. (Please note the author's name on this sample is not as it should be displayed in your rendering.)

```html
<!DOCTYPE html>
<html lang="en">
<head>
<meta charset="utf-8">
<title>Paper Crown — Cover Spread</title>
<link rel="stylesheet" href="https://fonts.googleapis.com/css2?family=Fjalla+One&family=Open+Sans:wght@400&display=swap">
<style>
  :root {
    --page: #ffffff;
    --back-red: #8d2a2d;
    --front-maroon: #6c2228;
    --glow-orange: #f19a2a;
    --glow-gold: #fbc453;
    --band-light: rgba(236, 220, 212, 0.9);
    --band-author: rgba(250, 238, 225, 0.88);
    --title-ink: #6b2128;
    --text-light: #ffffff;
  }
  * { margin: 0; padding: 0; box-sizing: border-box; }
  html, body {
    width: 1200px; height: 999px; overflow: hidden;
    background: var(--page);
  }
  .spread {
    position: absolute; left: 72px; top: 114px;
    width: 1056px; height: 770px;
  }
  .back-cover {
    position: absolute; left: 0; top: 0; width: 542px; height: 770px;
    background: radial-gradient(circle at 20% 85%, #a3403c 0%, transparent 45%),
                radial-gradient(circle at 90% 60%, #a13e3d 0%, transparent 40%),
                var(--back-red);
  }
  .back-art, .front-art { position: absolute; inset: 0; }
  .blurb {
    position: absolute; left: 26px; top: 32px; width: 455px;
    font-family: "Open Sans", Arial, sans-serif;
    font-size: 16.2px; line-height: 24.4px;
    color: var(--text-light); text-align: justify;
  }
  .blurb p + p { margin-top: 24.4px; }
  .site-url {
    position: absolute; right: 66px; top: 722px;
    font-family: "Open Sans", Arial, sans-serif;
    font-size: 16.2px; color: var(--text-light);
  }
  .front-cover {
    position: absolute; left: 542px; top: 0; width: 514px; height: 770px;
    background: var(--front-maroon);
    overflow: hidden;
  }
  .front-art {
    background:
      radial-gradient(ellipse at 75% 90%, var(--glow-gold) 0%, transparent 45%),
      radial-gradient(ellipse at 40% 95%, var(--glow-orange) 0%, transparent 50%),
      radial-gradient(ellipse at 95% 40%, rgba(241,154,42,0.45) 0%, transparent 35%),
      linear-gradient(180deg, var(--front-maroon) 0%, var(--front-maroon) 55%, #b65a2c 80%, #e88f2d 100%);
  }
  .title-band {
    position: absolute; left: 0; top: 56px; width: 514px; height: 127px;
    background: var(--band-light);
    display: flex; align-items: center; justify-content: center;
  }
  .title {
    font-family: "Fjalla One", "Arial Narrow", sans-serif;
    font-size: 90px; line-height: 1; letter-spacing: 1px;
    color: var(--title-ink); text-transform: uppercase; white-space: nowrap;
  }
  .tagline {
    position: absolute; left: 35px; top: 202px;
    font-family: "Fjalla One", "Arial Narrow", sans-serif;
    font-size: 50px; line-height: 67px;
    color: var(--text-light); text-transform: uppercase;
  }
  .author-band {
    position: absolute; left: 0; top: 694px; width: 514px; height: 60px;
    background: var(--band-author);
    display: flex; align-items: center; justify-content: center;
  }
  .author {
    font-family: "Fjalla One", "Arial Narrow", sans-serif;
    font-size: 44px; line-height: 1;
    color: var(--title-ink); text-transform: uppercase;
  }
</style>
</head>
<body>
  <div class="spread">
    <section class="back-cover">
      <div class="back-art" role="img" aria-label="Soft blurred bokeh light circles in deep red tones"></div>
      <div class="blurb">
        <p>Dale and Rhoda Pembury ran a successful courier company-until the Internet changed the way documents were delivered. Now, through a series of tragic events and poor financial decisions, Dale has begun to ask himself some tough questions.</p>
        <p>To what length would Dale go to save himself from the effects of poor financial decisions? How far can he sink to hide personal failure from his wife and children? Could he burn his house down to collect insurance? Could he fake his own death to give his family what they deserve? Or could he even kill his wife and children to end their struggles?</p>
        <p>While Dale is trapped in his own personal hell, Rhoda discovers what she thinks may be an anodyne for their financial ailments. Can it save them in time? Or will it destroy them all?</p>
        <p>Written by an experienced (now reformed) telemarketer, the insidious greed and trickery of the industry is revealed in a story that will find you grinding your teeth and clenching your jaw. Not only is Paper Crown entertaining, but it is a welcome manifesto of true confessions by a former insider of the industry.</p>
      </div>
      <div class="site-url">PaperCrownTheBook.test</div>
    </section>
    <section class="front-cover">
      <div class="front-art" role="img" aria-label="Blurred bokeh lights glowing orange and gold over deep maroon"></div>
      <div class="title-band"><h1 class="title">Paper Crown</h1></div>
      <p class="tagline">A Modern Tale<br>of Greed, Lust,<br>and Fear</p>
      <div class="author-band"><p class="author">Warren T. Ashby</p></div>
    </section>
  </div>
</body>
</html>
```